One page informative flyer for Florist

We are looking for a simple one page flyer. We are a florist who sell flowers, and commemorative t-shirts at graduation ceremonies, and need a flyer that can be given out to students so that they will know what is available on site. Further, we want the flyer to be editable (ie. a word template, or some other program), so that we can change the schools name, and change small bits of the copy easily.

What we are really looking for is a simple template, but we need 4 iterations of the flyer. With each of our two logos, I will need a flyer for t-shirts, and a flyer for flowers. Making 4 total. Please see breakdown below as explanation:

1, Tassel Lane Flowers logo - flyer for flowers
2. Tassel Lane Flowers logo - flyer for shirts
3. Brightmarch Flowers logo - flyer for flowers
4. Brightmarch Flowers logo - flyer for shirts

Please see logos for Tassel Lane Flowers and Brightmarch Flowers attached, as well as a picture of flowers and of the shirts. Feel free to use those images or stock images.

Here is the copy:

Flowers - A variety floral arrangements will be available for purchase at our stand, located conveniently at the graduation ceremony. You can browse our selection & pre-order ahead of time at: www.brightmarchflowers-example.com/index,php/test

T-Shirts - Commerative T-Shirts displaying all of the students names will be available for purchase at our stand, located conveniently at the graduation ceremony. You can pre-order ahead of time to guarantee your choice of size at: www.brightmarchflowers-example.com/index.php/test

```html
<!DOCTYPE html>
<html lang="en">
<head>
<meta charset="utf-8">
<title>Brightmarch Flowers – Graduation Flyers</title>
<link rel="stylesheet" href="https://fonts.googleapis.com/css2?family=Montserrat:wght@600;700&display=swap">
<style>
  :root {
    --page-bg: #ffffff;
    --sheet-top: #ffffff;
    --sheet-bottom: #ececec;
    --copy-grey: #6b6c6e;
    --note-grey: #86888a;
    --brand-green: #6fa83a;
    --band-light: #8cc152;
    --band-dark: #5e9a2c;
    --rose-red: #c8141c;
    --rose-deep: #7a0a0e;
    --rose-glow: #f3e6a8;
    --shirt-grey: #9a9a9a;
    --shirt-light: #d6d6d6;
    --label-ink: #111111;
  }
  * { box-sizing: border-box; margin: 0; padding: 0; }
  html, body { width: 1200px; height: 799px; overflow: hidden; background: var(--page-bg); }
  body { position: relative; font-family: "Montserrat", Arial, sans-serif; }

  .flyer {
    position: absolute; top: 9px; width: 567px; height: 732px; overflow: hidden;
    background: linear-gradient(180deg, var(--sheet-top) 40%, var(--sheet-bottom) 100%);
  }
  .flyer--flowers { left: 17px; }
  .flyer--shirts { left: 628px; }

  .hero { position: absolute; left: 0; top: 0; width: 100%; height: 345px; }
  .hero--roses {
    background:
      radial-gradient(circle at 65% 40%, var(--rose-red) 0%, var(--rose-red) 22%, transparent 45%),
      radial-gradient(circle at 25% 55%, var(--rose-red) 0%, transparent 30%),
      radial-gradient(circle at 10% 20%, var(--rose-glow) 0%, transparent 35%),
      linear-gradient(135deg, #f1e9b5 0%, #d24a3a 45%, var(--rose-deep) 100%);
  }
  .hero--shirt {
    background:
      radial-gradient(ellipse at 50% 40%, #f4f4f4 0%, #eaeaea 25%, transparent 45%),
      radial-gradient(circle at 50% 45%, var(--shirt-light) 0%, var(--shirt-grey) 80%);
  }

  .curve { position: absolute; left: 0; top: 0; width: 100%; height: 732px; }

  .copy {
    position: absolute; left: 50%; transform: translateX(-50%);
    text-align: center; color: var(--copy-grey);
    font-weight: 700; font-size: 16.5px; line-height: 18px;
  }
  .flyer--flowers .copy { top: 318px; width: 340px; }
  .flyer--shirts .copy { top: 325px; width: 480px; }

  .thumb { position: absolute; border-radius: 10px; box-shadow: 0 4px 6px rgba(0,0,0,0.15); }
  .thumb--red { left: 120px; top: 402px; width: 148px; height: 92px;
    background: radial-gradient(circle at 50% 50%, var(--rose-red) 0%, #8e1a1a 55%, #c9a57a 100%); }
  .thumb--pink { left: 292px; top: 402px; width: 148px; height: 92px;
    background: radial-gradient(circle at 50% 50%, #e89aa0 0%, #c97d80 55%, #c9a57a 100%); }
  .thumb--tees { left: 180px; top: 400px; width: 208px; height: 120px;
    background: linear-gradient(135deg, #ececec 0%, #cfcfcf 60%, #bdbdbd 100%); }

  .brand {
    position: absolute; left: 0; width: 100%; top: 528px; text-align: center;
    color: var(--brand-green); font-weight: 700; font-size: 50px; line-height: 58px;
    letter-spacing: -1px;
  }

  .note {
    position: absolute; left: 0; width: 100%; top: 672px; text-align: center;
    color: var(--note-grey); font-weight: 700; font-size: 13.5px;
  }

  .url-bar {
    position: absolute; left: 0; bottom: 0; width: 100%; height: 38px;
    background: linear-gradient(180deg, var(--band-light), var(--band-dark));
    color: #fff; font-weight: 700; font-size: 13.5px;
    display: flex; align-items: center; justify-content: center;
  }

  .size-label {
    position: absolute; top: 748px; font-size: 42px; font-weight: 600;
    color: var(--label-ink); letter-spacing: -1px;
  }
  .size-label--left { left: 17px; }
  .size-label--right { left: 628px; }
</style>
</head>
<body>

<section class="flyer flyer--flowers">
  <div class="hero hero--roses" role="img" aria-label="Close-up photo of red roses with soft yellow background"></div>
  <svg class="curve" viewBox="0 0 567 732" aria-hidden="true">
    <path d="M0,305 Q300,270 567,345 L567,732 L0,732 Z" fill="#fbfbfb"/>
    <path d="M0,288 Q300,255 567,325 L567,345 Q300,270 0,305 Z" fill="#78b243"/>
  </svg>
  <p class="copy">A variety floral arrangements will be available for purchase at our stand, located conveniently at the graduation ceremony</p>
  <div class="thumb thumb--red" role="img" aria-label="Bouquet of red roses"></div>
  <div class="thumb thumb--pink" role="img" aria-label="Bouquet of pink roses"></div>
  <div class="brand">Brightmarch<br>Flowers</div>
  <p class="note">You can browse our selection &amp; pre-order ahead of time at:</p>
  <div class="url-bar">www.brightmarchflowers-example.com/index,php/test</div>
</section>

<section class="flyer flyer--shirts">
  <div class="hero hero--shirt" role="img" aria-label="Photo of a white college T-shirt worn against a grey backdrop"></div>
  <svg class="curve" viewBox="0 0 567 732" aria-hidden="true">
    <path d="M0,305 Q300,270 567,345 L567,732 L0,732 Z" fill="#fbfbfb"/>
    <path d="M0,288 Q300,255 567,325 L567,345 Q300,270 0,305 Z" fill="#78b243"/>
  </svg>
  <p class="copy">Commerative T-Shirts displaying all of the students names will be available for purchase at our stand, located conveniently at the graduation ceremony.</p>
  <div class="thumb thumb--tees" role="img" aria-label="Two commemorative T-shirts, front with school name and back with graduating class names"></div>
  <div class="brand">Brightmarch<br>Flowers</div>
  <p class="note">You can pre-order ahead of time to guarantee your choice of size at:</p>
  <div class="url-bar">www.brightmarchflowers-example.com/index.php/test</div>
</section>

<p class="size-label size-label--left">8.5x11</p>
<p class="size-label size-label--right">8.5x11</p>

</body>
</html>
```